Real estate company needs a letterhead design

A young real estate company needs a letterhead / stationery design, it should include the company's logo. It should look exactly the same as on the business cards. (With the phrase "a brand of FEO Immobilien & Projektentwicklung GmbH")

In addition, it should also include the 4 round seals.

color code blue # 00456b gray # 333333

Word and PDF are welcome.

FEO Immobilien & Projektentwicklung GmbH
Managing director: Mag. Lukas Strenhofer
Anton-Wiesmayr-Strasse 3c / 41
6345 Almhofen

Tel .: +436645917283
Email: office@wohnquell.example
Web: www.wohnquell.example

Sparkasse Almhofen, Bergländer Sparkasse from 1893, Gildenkasse
Ferdinand-Moosrainer-Strasse 9, 6345 Almhofen
IBAN: AT31 4819 2093 5521 6604
BIC: GLMRAT31XXX
Account holder: FEO Immobilien & Projektentwicklung GmbH

FN: XXXXXXX
UID: XXXXXXX

```html
<!DOCTYPE html>
<html lang="de">
<head>
<meta charset="utf-8">
<title>Wohnquell – Briefpapier</title>
<link href="https://fonts.googleapis.com/css2?family=Fira+Sans:wght@400;500;700&display=swap" rel="stylesheet">
<style>
  :root{
    --brand-blue:#00456b;
    --brand-navy:#0b2c48;
    --text-gray:#333333;
    --paper:#ffffff;
    --backdrop:#e4e4e4;
    --ink-blue:#5b7fc9;
  }
  html,body{margin:0;padding:0;width:1200px;height:1200px;overflow:hidden;background:var(--backdrop);}
  body{font-family:"Fira Sans",sans-serif;color:var(--text-gray);}
  .sheet{
    position:absolute;left:204px;top:40px;width:792px;height:1120px;
    background:var(--paper);box-shadow:0 6px 24px rgba(0,0,0,.12);overflow:hidden;
  }
  .contact{
    position:absolute;left:540px;top:70px;font-size:10.5px;line-height:1.45;color:var(--text-gray);
    font-style:normal;
  }
  .contact__name{color:var(--brand-blue);font-weight:500;}
  .contact__label{color:var(--brand-blue);display:inline-block;width:38px;}
  .brand{
    position:absolute;left:62px;top:228px;display:flex;align-items:center;gap:10px;
  }
  .brand__mark{width:14px;height:14px;background:var(--brand-blue);}
  .brand__name{font-size:40px;font-weight:700;color:var(--brand-blue);letter-spacing:1px;}
  .letter{
    position:absolute;left:238px;top:408px;width:500px;font-size:13px;line-height:2.05;color:var(--text-gray);
  }
  .letter__recipient{margin:0 0 18px;line-height:1.7;}
  .letter__recipient span{display:block;}
  .letter__recipient span + span{padding-left:14px;}
  .letter p{margin:0 0 28px;}
  .closing{margin-top:34px;font-size:13px;}
  .signature{display:block;margin-top:8px;width:210px;height:34px;background:linear-gradient(90deg,rgba(91,127,201,.35),rgba(91,127,201,.12));border-radius:3px;}
  .bank{
    position:absolute;right:40px;top:940px;width:640px;text-align:right;font-size:12.5px;line-height:1.7;color:var(--text-gray);
  }
  .bank__label{color:var(--brand-blue);}
  .bank__sep{color:var(--brand-blue);padding:0 3px;}
  .band{position:absolute;left:0;bottom:0;width:792px;height:60px;}
</style>
</head>
<body>
  <main class="sheet">
    <address class="contact">
      <div class="contact__name">Mag. Lukas Strenhofer</div>
      <div>Managing director</div>
      <div><span class="contact__label">Tel</span>: +436645917283</div>
      <div><span class="contact__label">Web</span>: www.wohnquell.example</div>
      <div><span class="contact__label">Email</span>: office@wohnquell.example</div>
      <div>Anton-Wiesmayr-Strasse 3c / 41,</div>
      <div>6345 Almhofen</div>
    </address>

    <div class="brand">
      <span class="brand__mark"></span>
      <span class="brand__name">WOHNQUELL</span>
    </div>

    <section class="letter">
      <div class="letter__recipient"><span>To</span><span>The,</span><span>Director</span></div>
      <p>Lorem ipsum dolor sit amet, consectetur adipiscing elit. Sed at ante. Mauris eleifend, quam a vulptate dictum, massa quam dapibus leo, eget vulputate orci purus ut lorem. In fringilla mi in ligula. Pellen tesque aliquam quam vel dolor. Nunc adipiscing. Sed quamodio, tempus ac, aliquam molestie varius ac, tellus. Vestibulum ut nulla aliquam risus rutrum interdum. Pellentesque lorem.</p>
      <p>Curabitur sit amet erat quis risus feugiat viverra. Pellentesque augue justo sagittis et, lacinia at, venenatis non, arcu. Nunc nec libero. In cursus dictum risus. Etiam tristique nisl a nulla.</p>
      <div class="closing">
        Thanking you,
        <span class="signature" role="img" aria-label="Handwritten signature of Mag. Lukas Strenhofer"></span>
      </div>
    </section>

    <footer class="bank">
      <div><span class="bank__label">Account holder:</span> FEO Immobilien &amp; Projektentwicklung GmbH</div>
      <div><span class="bank__label">IBAN</span> : AT31 4819 2093 5521 6604<span class="bank__sep">|</span><span class="bank__label">BIC</span> : GLMRAT31XXX<span class="bank__sep">|</span><span class="bank__label">FN</span> : XXXXXXX<span class="bank__sep">|</span><span class="bank__label">UID</span> : XXXXXXX</div>
      <div>Sparkasse Almhofen, Bergländer Sparkasse from 1893, Gildenkasse, Ferdinand-Moosrainer-Strasse 9, 6345 Almhofen</div>
    </footer>

    <svg class="band" viewBox="0 0 792 60" aria-hidden="true">
      <polygon points="0,38 560,38 548,60 0,60" fill="var(--brand-blue)"/>
      <polygon points="572,14 792,14 792,60 556,60" fill="var(--brand-navy)"/>
    </svg>
  </main>
</body>
</html>
```